Modern and sophisticated web design for architect/designer

Lumo Vant is a Building Design & Drafting studio based in Nedlands Western Australia, providing a high quality and complete client service from concept design through Council planning approvals and building licenses to construction drawings for kitchens and bathrooms, extensions, additions, renovations and new homes.

Lumo Vant is looking for a new qwerty design that *is different from a normal* 2/3 column website. The website design must be very arty, clean and catchy. This design needs to be very different and must not look like a downloadable template.

The design must be able to display a lot of photos for the different projects.

The design must comply with W3C standards (i.e. use of fonts) and must be delivered to us in A PSD layered format.

Here are a couple of example website designs that exemplify what I am after:
1) http://www.prtd.com.au/
2) http://www.martinholsbyarchitect.com/en/
3) http://veromiks.com/

I particularly like numbers 1 and 2. The third, Veromiks, jumps around a little between pages as it is actually several companies. I prefer the page design to remain steady if possible.

I like the very clever nature of number 1 (PRTD). It captures the interest, although slightly gimmicky, however I think it doesn't overpower. Its modern, and visual.

I like the clean elegant design of number 2 (Holsby), it simply delivers everything necessary in a clear intelligent manner, its attractive, menu is clever simple to use and attractive.

I would be very happy to have either of these websites.

here is another one:
4) http://www.tqarchitect.com.au/

Although this is similarly elegant, it appears quite dated. I don't like the thumbnails that you click on in the gallery, its quite clumsy. It looks minimalist, and IS minimalist, doesn't look like there is much option to expand other than changing the pictures.

If you look at my own website:
http://www.lumovant.com.au

I designed and built it myself without any skills or experience. I had to use a generic photo album generator which was worse than useless, the point I am trying to make is I tried to make the menu system a little unusual, I tried to keep the pages neat and tidy, and totally used the "black website" method. However I am more inclined to go with the lighter/white pages of (1) and (2) above because they tend to show photos better.

Dear Designers. 

ArtHive Administration has worked to provide a more comprehensive brief. Please review the amended description. 

Kind Regards, Wesley. 

Target Market(s)

Target market is people who are looking to renovate their home

Industry/Entity Type

Construction

Requirements
Must have
• The brief is to design a visual modern, elegant, sophisticated website for a small scale designer/photographer/architect that looks itself like it is designed. Not off the shelf, simple and dated. Basically the design itself has to exemplify me, it has to say "this guy is a designer, and he is good at it".

```html
<!DOCTYPE html>
<html lang="en">
<head>
<meta charset="utf-8">
<title>Lumo Vant – Building Design &amp; Drafting</title>
<link rel="stylesheet" href="https://fonts.googleapis.com/css2?family=Open+Sans:wght@400;600;700&display=swap">
<style>
:root{
  --ink:#222;
  --text:#555;
  --muted:#777;
  --band-edge:#2a2a2a;
  --page:#ffffff;
  --nav-top:#3c3c3c;
  --nav-bottom:#0b0b0b;
  --accent:#f28c12;
  --green:#5cb82e;
  --frame:#d0d0d0;
}
*{margin:0;padding:0;box-sizing:border-box}
html,body{width:797px;height:1200px;overflow:hidden}
body{position:relative;background:var(--page);font-family:"Open Sans",Arial,sans-serif;color:var(--text)}
.side-band{position:absolute;top:0;height:307px;background:linear-gradient(90deg,#040404,var(--band-edge) 50%,#040404)}
.side-band.left{left:0;width:59px}
.side-band.right{left:738px;width:59px}
.sheet{position:absolute;left:59px;top:0;width:679px;height:1200px;background:var(--page);box-shadow:0 0 8px rgba(0,0,0,.4)}
.abs{position:absolute}

.brand{left:12px;top:16px;display:flex;align-items:center;gap:10px}
.brand-mark{width:16px;height:16px;background:#444}
.brand-name{font-size:21px;font-weight:600;letter-spacing:5px;color:#333;text-transform:uppercase;line-height:1}
.search{left:506px;top:29px;width:160px;height:21px;border:1px solid #ddd;border-radius:3px;background:#f7f7f7;font-size:10px;color:#999;padding:3px 8px;box-shadow:inset 0 1px 2px rgba(0,0,0,.08)}
.search-btn{left:649px;top:27px}

.main-nav{left:0;top:80px;width:679px;height:28px;display:flex;background:linear-gradient(var(--nav-top),#1c1c1c 50%,var(--nav-bottom));box-shadow:inset 0 1px 0 rgba(255,255,255,.15)}
.main-nav a{display:flex;align-items:center;justify-content:center;color:#fff;font-size:10px;font-weight:700;text-decoration:none;border-right:1px solid #4a4a4a;height:100%;letter-spacing:.2px}
.main-nav a:last-child{border-right:0}

.call{left:488px;top:118px;display:flex;align-items:center;gap:12px;font-size:12px;color:#333}

.slider{left:32px;top:144px;width:616px;height:307px;border:1px solid var(--frame);padding:7px;background:#fff;box-shadow:0 1px 3px rgba(0,0,0,.12)}
.photo{width:100%;height:100%}
.slide-photo{background:
  radial-gradient(ellipse 30% 40% at 52% 48%,#f0b45a 0%,rgba(200,120,40,.6) 40%,transparent 75%),
  linear-gradient(180deg,#0c2a44 0%,#1a3140 40%,#2c2a18 70%,#1a1d10 100%)}
.dots{left:297px;top:468px;width:85px;height:23px;border-radius:6px;background:linear-gradient(#2a2a2a,#050505);display:flex;align-items:center;justify-content:center;gap:9px}
.dots span{width:10px;height:10px;border-radius:50%;background:#777}
.dots span.on{background:#fff}

.section-title{font-size:14px;font-weight:400;color:var(--ink);text-transform:uppercase;line-height:1;letter-spacing:.2px}
.welcome-title{left:32px;top:499px}
.welcome-photo{left:32px;top:525px;width:233px;height:162px;background:linear-gradient(180deg,#4d86d2 0%,#8fb0d6 40%,#b8aa98 58%,#7a7068 75%,#4e6a3a 100%)}
.welcome-copy{left:284px;top:527px;width:361px;font-size:9px;line-height:14px;color:#666}
.welcome-copy p+p{margin-top:12px}
.read-more{left:284px;top:663px;width:73px;height:19px;border-radius:4px;background:linear-gradient(#3a3a3a,#050505);color:#fff;font-size:8px;font-weight:700;display:flex;align-items:center;justify-content:center;gap:5px}

.dotted-rule{left:32px;top:712px;width:613px;border-top:1px dotted #999}

.services-title{left:32px;top:729px}
.service-list{left:32px;top:752px;width:280px;list-style:none;display:grid;grid-template-columns:166px 114px;row-gap:11px}
.service-list li{font-size:11px;color:#333;display:flex;align-items:center;gap:7px;height:18px;white-space:nowrap}
.service-list li::before{content:"";border-left:7px solid var(--accent);border-top:5px solid transparent;border-bottom:5px solid transparent}
.divider{left:321px;top:730px;height:190px;border-left:1px dotted #999}

.blog-title{left:342px;top:729px}
.post{left:341px;width:304px;height:74px}
.post-thumb{position:absolute;left:0;top:0;width:104px;height:73px}
.thumb-kitchen{background:linear-gradient(135deg,#2e2018,#8a5a32 45%,#c9b79a 80%,#e0d6c6)}
.thumb-house{background:linear-gradient(170deg,#1d3f6a,#3a4a4a 45%,#8a5a22 65%,#24331a)}
.post-body{position:absolute;left:114px;top:0;width:192px}
.post-body h3{font-size:11px;font-weight:400;color:#222;white-space:nowrap;line-height:14px}
.post-body p{font-size:9px;line-height:13px;color:#666;margin-top:6px}
.post-meta{display:flex;align-items:center;gap:4px;margin-top:9px;font-size:8px;color:#444;white-space:nowrap}
.pill{border:1px solid #bbb;border-radius:2px;padding:0 4px;background:linear-gradient(#fff,#e6e6e6);color:#335;line-height:11px}
.count{border:1px solid #ccc;padding:0 3px;background:#fff;line-height:11px}

.featured-title{left:32px;top:943px}
.featured-band{left:32px;top:967px;width:614px;height:120px;background:linear-gradient(#040404,#1e1e1e 45%,#3a3a3a 65%,#0a0a0a)}
.work-thumb{position:absolute;top:26px;width:129px;height:68px;border:2px solid #fff;box-shadow:0 2px 6px rgba(0,0,0,.6)}
.w1{background:linear-gradient(150deg,#2a2d33,#8b8e93 55%,#3c3e41)}
.w2{background:linear-gradient(180deg,#3f7fd4,#c9ced3 55%,#7a6e5e)}
.w3{background:linear-gradient(180deg,#6aa0d8,#f0f0f0 50%,#3f7a2a)}
.w4{background:linear-gradient(180deg,#2a68c4,#8fb8e6 45%,#eef0f2)}
.arrow-l{left:12px;top:55px;border-right:7px solid #666;border-top:6px solid transparent;border-bottom:6px solid transparent}
.arrow-r{left:596px;top:55px;border-left:7px solid #666;border-top:6px solid transparent;border-bottom:6px solid transparent}

.footer-rule{left:0;top:1117px;width:679px;border-top:1px solid #ccc}
.footer-links{left:10px;top:1135px;font-size:9px;color:#333;letter-spacing:.3px}
.footer-bar{left:0;top:1165px;width:679px;height:35px;background:linear-gradient(#1a1a1a,#000);display:flex;align-items:center;justify-content:space-between;padding:0 10px;color:#ccc;font-size:9px}
.social{display:flex;gap:7px}
.social span{width:20px;height:20px;border-radius:2px;background:linear-gradient(#f2f2f2,#c8c8c8)}
</style>
</head>
<body>
<div class="side-band left"></div>
<div class="side-band right"></div>

<div class="sheet">
  <header>
    <div class="abs brand"><span class="brand-mark"></span><span class="brand-name">Lumo Vant</span></div>
    <div class="abs search">Search...</div>
    <svg class="abs search-btn" width="24" height="24" viewBox="0 0 24 24" aria-hidden="true">
      <circle cx="12" cy="12" r="11" fill="var(--green)"/>
      <circle cx="10.5" cy="10.5" r="4.5" fill="none" stroke="#fff" stroke-width="2"/>
      <line x1="14" y1="14" x2="18" y2="18" stroke="#fff" stroke-width="2.4" stroke-linecap="round"/>
    </svg>
    <nav class="abs main-nav">
      <a style="width:89px">Home</a>
      <a style="width:116px">About Us</a>
      <a style="width:123px">Services</a>
      <a style="width:128px">Our Work</a>
      <a style="width:121px">Specials</a>
      <a style="width:102px">Contact Us</a>
    </nav>
  </header>

  <div class="abs call">
    <svg width="22" height="22" viewBox="0 0 22 22" aria-hidden="true">
      <circle cx="11" cy="11" r="10.5" fill="var(--green)"/>
      <path d="M7 6.5c1-.6 1.6 0 2 1l.6 1.4c.2.6-.2 1-.7 1.3.6 1.3 1.5 2.2 2.8 2.8.3-.5.7-.9 1.3-.7l1.4.6c1 .4 1.6 1 1 2-.8 1.3-2.4 1.6-4.2.6-2-1.1-3.5-2.6-4.6-4.6-1-1.8-.7-3.4.4-4.4z" fill="#fff"/>
    </svg>
    <span>CALL US : 465 320 7714</span>
  </div>

  <section class="abs slider">
    <div class="photo slide-photo" role="img" aria-label="Modern stone and timber home lit warmly at dusk behind a landscaped garden"></div>
  </section>
  <div class="abs dots"><span class="on"></span><span></span><span></span><span></span></div>

  <h2 class="abs section-title welcome-title">Welcome</h2>
  <div class="abs welcome-photo" role="img" aria-label="Contemporary two-storey rendered house under a blue sky"></div>
  <div class="abs welcome-copy">
    <p>Donec quam felis, ultricies nec, pellentesque eu, pretium quis, sem. Nulla consequat massa quis enim. Donec pede justo, fringilla vel, aliquet nec, vulputate eget, arcu. In enim justo, rhoncus ut, imperdiet a, venenatis vitae, justo. Nullam dictum felis eu pede mollis pretium. Lorem ipsum dolor sit amet, consectetuer adipiscing elit. Aenean commodo ligula eget dolor. Lorem ipsum dolor.</p>
    <p>Cum sociis natoque penatibus et magnis dis parturient montes, nascetur ridiculus mus. Cum sociis natoque penatibus et magnis dis parturient.</p>
  </div>
  <div class="abs read-more">
    <svg width="6" height="7" viewBox="0 0 6 7" aria-hidden="true"><path d="M0 0L6 3.5 0 7z" fill="#fff"/></svg>READ MORE
  </div>

  <div class="abs dotted-rule"></div>

  <h2 class="abs section-title services-title">Our Services</h2>
  <ul class="abs service-list">
    <li>Fcena massa cum vbciosd</li><li>Suspdisse metus</li>
    <li>Ncina bbsa cum</li><li>Ygena tevsm</li>
    <li>Rceena tevsa bsm</li><li>Rceena tevsa bsm</li>
    <li>Duis solicit</li><li>Duis solicit</li>
    <li>Bfis solicit</li><li>Ncina bbsa cum</li>
    <li>Qiss Pseicit</li>
  </ul>
  <div class="abs divider"></div>

  <h2 class="abs section-title blog-title">Blog</h2>
  <article class="abs post" style="top:753px">
    <div class="post-thumb thumb-kitchen" role="img" aria-label="Modern kitchen interior with timber cabinetry"></div>
    <div class="post-body">
      <h3>Dsena massa cum vceena tevsa bsse.</h3>
      <p>Arena massa cum vceena tevsa bsse metus massa cum vceena tevsa bsse metus.</p>
      <div class="post-meta"><span class="pill">Like</span><span class="count">3k</span>&nbsp;<span class="pill">Tweet</span><span class="count">316</span>&nbsp;2 Aug 2013</div>
    </div>
  </article>
  <article class="abs post" style="top:844px">
    <div class="post-thumb thumb-house" role="img" aria-label="House exterior lit at night"></div>
    <div class="post-body">
      <h3>Cfna massa cum vceena tevsa bsse.</h3>
      <p>Arena massa cum vceena tevsa bsse metus massa cum vceena tevsa bsse metus.</p>
      <div class="post-meta"><span class="pill">Like</span><span class="count">3k</span>&nbsp;<span class="pill">Tweet</span><span class="count">316</span>&nbsp;2 Aug 2013</div>
    </div>
  </article>

  <h2 class="abs section-title featured-title">Featured Work</h2>
  <section class="abs featured-band">
    <span class="abs arrow-l"></span>
    <div class="work-thumb w1" style="left:28px" role="img" aria-label="Curved concrete and glass residence"></div>
    <div class="work-thumb w2" style="left:171px" role="img" aria-label="Two-storey house with timber balcony"></div>
    <div class="work-thumb w3" style="left:313px" role="img" aria-label="White modern villa above a lawn"></div>
    <div class="work-thumb w4" style="left:456px" role="img" aria-label="Tall white building facade against blue sky"></div>
    <span class="abs arrow-r"></span>
  </section>

  <footer>
    <div class="abs footer-rule"></div>
    <div class="abs footer-links">HOME | ABOUT US | NEWS | BLOG | SPECIALS | TESTIMONIALS | CONTACT US</div>
    <div class="abs footer-bar">
      <span>Copyright © 2013 lumovant.com</span>
      <div class="social"><span></span><span></span><span></span><span></span><span></span></div>
    </div>
  </footer>
</div>
</body>
</html>
```